Pediatric Dentist Business Card

I need a business card designed for a dentist who works exclusively with children.
We prefer designs that are out of ordiary that is fun and interesting to kids.

there is no logo since this is a dentists office. The name of the doctor is "Tavor Kesh" if you want to get creative with that.

Target Market(s)

Kids

Industry/Entity Type

Business

Contact Information for Business Card

Anythings that is creative

Colors

Designer to choose colors to be used in the design.

```html
<!DOCTYPE html>
<html lang="en">
<head>
<meta charset="utf-8">
<title>Sunny Molars – Business Card</title>
<link rel="stylesheet" href="https://fonts.googleapis.com/css2?family=Roboto:wght@400;500;700&display=swap">
<style>
  :root {
    --backdrop: #e9e6e1;
    --front-top: #3c77dc;
    --front-bottom: #4689f2;
    --front-ink: #eef3fb;
    --back-bg: #16191b;
    --teeth: #f4f4f2;
    --accent-blue: #3b7be8;
    --name-bar: #eceef2;
    --contact-ink: #f2f2f2;
    --figure-light: #d9dde3;
    --figure-dark: #8a6a4a;
  }
  * { margin: 0; padding: 0; box-sizing: border-box; }
  html, body { width: 1200px; height: 800px; overflow: hidden; }
  body {
    background: var(--backdrop);
    font-family: "Roboto", Arial, sans-serif;
    position: relative;
  }
  .card {
    position: absolute;
    top: 60px;
    width: 400px;
    height: 680px;
    overflow: hidden;
    box-shadow: 0 6px 18px rgba(0,0,0,0.25);
  }

  /* Front */
  .card-front {
    left: 170px;
    background: linear-gradient(180deg, var(--front-top), var(--front-bottom));
  }
  .brand {
    position: absolute;
    top: 250px;
    left: 0;
    width: 100%;
    display: flex;
    flex-direction: column;
    align-items: center;
    gap: 14px;
  }
  .brand-mark {
    width: 46px;
    height: 46px;
    border-radius: 50%;
    background: var(--front-ink);
  }
  .brand-name {
    color: var(--front-ink);
    font-weight: 500;
    font-size: 34px;
    letter-spacing: 12px;
    text-align: center;
    line-height: 1.3;
    padding-left: 12px;
  }

  /* Back */
  .card-back {
    left: 630px;
    background: var(--back-bg);
  }
  .teeth-row {
    position: absolute;
    left: 0;
    width: 100%;
    height: 44px;
    background: linear-gradient(180deg, var(--teeth), #dcdcda);
  }
  .teeth-row.upper { top: 0; }
  .teeth-row.lower { bottom: 0; background: linear-gradient(0deg, var(--teeth), #dcdcda); }
  .dentist-figure {
    position: absolute;
    top: 112px;
    left: 150px;
    width: 150px;
    height: 190px;
    border-radius: 18px;
    background: linear-gradient(180deg, var(--figure-light) 0%, #c7cdd6 65%, var(--figure-dark) 100%);
  }
  .name-band {
    position: absolute;
    top: 298px;
    left: 0;
    width: 100%;
    height: 96px;
    background: linear-gradient(90deg, #1c1f21 0%, #24282a 50%, transparent 50%);
  }
  .name-bar {
    position: absolute;
    top: 318px;
    left: 130px;
    width: 270px;
    height: 76px;
    background: linear-gradient(90deg, #6b6e72 0%, var(--name-bar) 12%, var(--name-bar) 100%);
    display: flex;
    align-items: center;
    padding-left: 42px;
  }
  .doctor-name {
    color: var(--accent-blue);
    font-weight: 700;
    font-size: 38px;
    white-space: nowrap;
  }
  .contacts {
    position: absolute;
    top: 420px;
    left: 40px;
    list-style: none;
    display: flex;
    flex-direction: column;
    gap: 26px;
  }
  .contact {
    display: flex;
    align-items: center;
    gap: 18px;
    color: var(--contact-ink);
    font-weight: 500;
    font-size: 24px;
  }
  .contact-icon { width: 38px; height: 38px; flex: none; }
</style>
</head>
<body>

<section class="card card-front">
  <div class="brand">
    <span class="brand-mark"></span>
    <p class="brand-name">SUNNY<br>MOLARS</p>
  </div>
</section>

<section class="card card-back">
  <div class="teeth-row upper" role="img" aria-label="Row of upper cartoon teeth along the top edge"></div>

  <div class="dentist-figure" role="img" aria-label="Cartoon dentist in a white coat holding dental tools"></div>

  <div class="name-band"></div>
  <div class="name-bar">
    <h1 class="doctor-name">Tavor Kesh</h1>
  </div>

  <ul class="contacts">
    <li class="contact">
      <svg class="contact-icon" viewBox="0 0 38 38" aria-hidden="true">
        <path d="M10 5 L15 5 L18 13 L14 16 C16 21 18 23 23 25 L26 21 L34 24 L34 29 C34 32 31 34 28 33 C17 31 8 22 6 11 C5 8 7 5 10 5 Z" fill="var(--accent-blue)"/>
      </svg>
      <span>155-246-780</span>
    </li>
    <li class="contact">
      <svg class="contact-icon" viewBox="0 0 38 38" aria-hidden="true">
        <circle cx="19" cy="19" r="18" fill="var(--accent-blue)"/>
        <text x="19" y="26" text-anchor="middle" font-family="Roboto, Arial, sans-serif" font-weight="700" font-size="22" fill="#ffffff">@</text>
      </svg>
      <span>hello@sunnymolars.com</span>
    </li>
    <li class="contact">
      <svg class="contact-icon" viewBox="0 0 38 38" aria-hidden="true">
        <circle cx="19" cy="19" r="18" fill="var(--accent-blue)"/>
        <rect x="0" y="13" width="38" height="12" fill="#ffffff"/>
        <text x="19" y="23" text-anchor="middle" font-family="Roboto, Arial, sans-serif" font-weight="700" font-size="10" fill="var(--accent-blue)">www</text>
      </svg>
      <span>www.sunnymolars.com</span>
    </li>
  </ul>

  <div class="teeth-row lower" role="img" aria-label="Row of lower cartoon teeth along the bottom edge"></div>
</section>

</body>
</html>
```